Calloway Ridge Associates Stationery

Use attached logo for stationery
Stationery, Letterhead and Envelope + Business cards

Tag line: Standing beside those who serve with faith and hope

```html
<!DOCTYPE html>
<html lang="en">
<head>
<meta charset="utf-8">
<title>Calloway Ridge Associates – Business Cards</title>
<link href="https://fonts.googleapis.com/css2?family=Mulish:wght@400;600;800&display=swap" rel="stylesheet">
<style>
  :root {
    --backdrop: #e3e5e7;
    --card-light: #eef0f1;
    --card-dark: #3a3b3e;
    --navy: #0c4a8e;
    --sky: #6ccbf0;
    --sun: #f6c31c;
    --ink-soft: #6f7377;
    --white: #ffffff;
  }
  * { box-sizing: border-box; margin: 0; padding: 0; }
  html, body {
    width: 1200px; height: 1200px; overflow: hidden;
    background: var(--backdrop);
    font-family: "Mulish", Arial, sans-serif;
  }
  .sheet {
    width: 1200px; height: 1200px;
    display: flex; flex-direction: column; align-items: center; justify-content: center;
    gap: 60px;
  }
  .card {
    position: relative; width: 840px; height: 480px; overflow: hidden;
    box-shadow: 0 6px 18px rgba(0,0,0,.12);
  }

  /* Front */
  .card--front { background: var(--card-light); }
  .card__waves { position: absolute; inset: 0; width: 100%; height: 100%; }
  .brand {
    position: absolute; left: 50px; top: 180px; width: 330px;
    display: flex; align-items: center; gap: 12px;
  }
  .brand__dot { width: 18px; height: 18px; border-radius: 50%; background: var(--sun); flex: none; }
  .brand__name { font-weight: 800; font-size: 25px; line-height: 1.15; color: var(--navy); letter-spacing: .02em; text-transform: uppercase; }
  .divider { position: absolute; left: 410px; top: 78px; width: 1.5px; height: 200px; background: var(--sky); }
  .divider::after { content: ""; position: absolute; left: 0; bottom: 0; width: 120px; height: 1.5px; background: var(--sky); }
  .contact { position: absolute; left: 440px; top: 78px; color: var(--ink-soft); font-size: 15px; line-height: 1.6; }
  .contact__name { font-weight: 800; font-size: 22px; color: var(--navy); letter-spacing: .02em; margin-bottom: 4px; }
  .contact__row { display: flex; align-items: center; gap: 9px; }
  .contact__row svg { width: 14px; height: 14px; fill: var(--sky); flex: none; }
  .website { position: absolute; right: 40px; bottom: 30px; color: var(--white); font-size: 15px; letter-spacing: .03em; }

  /* Back */
  .card--back { background: var(--card-dark); border-bottom: 8px solid var(--sky); }
  .brand--center {
    left: 0; right: 0; top: 165px; width: auto; justify-content: center;
  }
  .brand--center .brand__name { color: var(--white); font-size: 34px; }
  .brand--center .brand__dot { width: 22px; height: 22px; }
  .tagline {
    position: absolute; left: 0; right: 0; top: 320px;
    display: flex; justify-content: center; align-items: center; gap: 12px;
    color: var(--white); font-size: 18px; letter-spacing: .01em;
  }
  .tagline__mark { width: 8px; height: 8px; background: var(--sky); transform: rotate(45deg); }
</style>
</head>
<body>
<main class="sheet">

  <section class="card card--front">
    <svg class="card__waves" viewBox="0 0 840 480" preserveAspectRatio="none" aria-hidden="true">
      <path d="M150 480 C 420 430, 650 370, 840 230" fill="none" stroke="var(--sun)" stroke-width="5"/>
      <path d="M240 480 C 480 425, 680 360, 840 250 L840 480 Z" fill="var(--sky)"/>
      <path d="M290 480 C 520 435, 700 385, 840 295 L840 480 Z" fill="var(--navy)"/>
    </svg>

    <div class="brand">
      <span class="brand__dot"></span>
      <span class="brand__name">Calloway Ridge Associates</span>
    </div>

    <div class="divider"></div>

    <div class="contact">
      <p class="contact__name">DANIEL R. HOLLIS</p>
      <p>Resident Manager</p>
      <p>48 Orchard Bend Road</p>
      <p>Fairview, SC 29000</p>
      <p class="contact__row">
        <svg viewBox="0 0 24 24"><path d="M6.6 10.8a15.1 15.1 0 0 0 6.6 6.6l2.2-2.2a1 1 0 0 1 1-.25 11.4 11.4 0 0 0 3.6.57 1 1 0 0 1 1 1V20a1 1 0 0 1-1 1A17 17 0 0 1 3 4a1 1 0 0 1 1-1h3.5a1 1 0 0 1 1 1c0 1.25.2 2.45.57 3.57a1 1 0 0 1-.25 1z"/></svg>
        (555) 014-3827
      </p>
      <p class="contact__row">
        <svg viewBox="0 0 24 24"><path d="M6 3h12v5H6zM4 9h16a2 2 0 0 1 2 2v6h-4v4H6v-4H2v-6a2 2 0 0 1 2-2zm4 7v3h8v-3z"/></svg>
        (555) 014-3828
      </p>
      <p class="contact__row">
        <svg viewBox="0 0 24 24"><path d="M2 5h20v14H2zm2 2v.5l8 5 8-5V7zm0 2.8V17h16V9.8l-8 5z"/></svg>
        info@callowayridge.org
      </p>
    </div>

    <p class="website">www.callowayridge.org</p>
  </section>

  <section class="card card--back">
    <div class="brand brand--center">
      <span class="brand__dot"></span>
      <span class="brand__name">Calloway Ridge Associates</span>
    </div>
    <p class="tagline">
      <span class="tagline__mark"></span>
      Standing beside those who serve with faith and hope
      <span class="tagline__mark"></span>
    </p>
  </section>

</main>
</body>
</html>
```